Wine labels Velmora Wine Council - Nueva etiqueta El Consejo Regulador de vinos de Albarrán

Velmora Wines Council, based in southern Spain, are looking to create a new suite of wine labels which retain the elegance of the Sherry Wines industry while reinvigorating their image to the modern era and a new generation of Sherry Wine lovers. These labels will be used across the Velmora Wines Council's range of wines for the promotion of the Sherry Wines industry.

Your design must present at least two styles of Sherry Wines which demonstrate an elegant, modern interpretation and understanding of the unique mood and personality for these wines and the essence of southern Spain.

10 labels will be created based on the winning design, one for each of the unique varieties of Sherry Wines within the collection. This collection comprises of several different wine varieties including: Fino, Manzanilla, Amontillado, Oloroso, Palo Cortado, Medium, Cream, Pale Cream, Pedro Ximenez and Moscatel.

We recommend you visit our website www.velmora-vinos.example/wines as the source to understanding the origins and unique personality of these diverse wines.

El Consejo Regulador de los Vinos de Albarrán y Tordesal quiere renovar las etiquetas de los vinos utilizados para sus actividades de promoción genérica. Esta colección de vinos comprende las tipologías más importantes de la región que incluye: fino, manzanilla, amontillado, oloroso, palo cortado, pale cream, medium, cream, pedro ximénez y moscatel. Por lo tanto se precisan 10 etiquetas, una para cada uno de los vinos mencionados.
Updates

Project Deadline Extended
Reason: Due to some confusion with the deadline we wish to officially extend the deadline to allow designers one last week to submit their entries.

Target Market(s)

Industry, journalists, media, sommeliers, chefs, wine writers

Industry/Entity Type

Council

Requirements
Must have
• Front and Back label plus capsule:
• Front label can have either of the two official logos of the Velmora Wine council titled Vinos de Albarrán Digital or not, this is optional. Must include: Vino selecionado por el Consejo Regulador de la Denominacion de Origen, Name of the variety of wine eg FINO, percentage of alcohol eg 15% and quantity 75 cl.
• The back of the label must include the council logo titled Sellora and 4 additional logos positioned smaller. The Europa logo must appear larger than the 3 other logos. Space for descriptive text about the wine is also required.
• The dimensions of the bottle can be found at this link http://www.vidrialto.example/es/catalogo/vinos-y-espumosos/bordelesas/bd-orla
• Altura:305 mm
• Diámetro base:76,20 mm
• Diámetro hombro:82 mm
• Tipo boca:Cetie
• Peso:750 gr
• Capacidad:75 cl
• Etiqueta delantera y trasera y capsula
• La etiqueta delantera puede incluir el logo oficial del Consejo Regulador o el logo digital, o ninguno, esto es opcional. Debe incluir el siguiete texto: Vino selecionado por el Consejo Regulador de la Denominacion de Origen, el nombre de la variedad del vino, por ejemplo Fino, el porcentaje de alcohol, por ejemplo 15%, y la capacidad 75cl.
• La etiqueta trasera debe incluir el logo oficial Sellora del Consejo, y cuatro logos adicionales con una dimension menor. El Logo de ¨Europa invierte en las zonas rurales¨ debe ser de mayor tamaño que los otros. Se precisa espacio para el texto descriptivo de los vinos.
• Las dimensiones de la botella se puede encontrar en este enlace
• http://www.vidrialto.example/es/catalogo/vinos-y-espumosos/bordelesas/bd-orla
• Altura:305 mm
• Diámetro base:76,20 mm
• Diámetro hombro:82 mm
• Tipo boca:Cetie
• Peso:750 gr
• Capacidad:75 cl
Nice to have
• See our website velmora-vinos.example to understand the origin of the wines. Ver nuestra página web velmora-vinos.example para mejor entender los vinos.
Should not have
• Images of catavinos or stereotypical images from Spain such as flamenco dancers or guitars.

```html
<!DOCTYPE html>
<html lang="es">
<head>
<meta charset="utf-8">
<title>Velmora Wine Council — Etiqueta Fino</title>
<link rel="stylesheet" href="https://fonts.googleapis.com/css2?family=Old+Standard+TT:ital,wght@0,700;1,400&display=swap">
<style>
  :root {
    --backdrop: #000000;
    --label-dark: #7a5a2e;
    --label-mid: #a3834f;
    --label-light: #c2a46c;
    --band: #d8cdb8;
    --ink: #2a1c0e;
    --ornament: #8d6c3f;
  }
  html, body {
    margin: 0;
    padding: 0;
    width: 1200px;
    height: 4072px;
    overflow: hidden;
    background: var(--backdrop);
  }
  .canvas {
    position: relative;
    width: 1200px;
    height: 4072px;
    font-family: "Old Standard TT", "Times New Roman", serif;
    color: var(--ink);
  }

  /* Neck label */
  .neck-label {
    position: absolute;
    left: 460px;
    top: 624px;
    width: 327px;
    height: 264px;
    border-radius: 50%;
    background: radial-gradient(ellipse at center, var(--label-light) 0%, var(--label-mid) 60%, var(--label-dark) 100%);
    box-sizing: border-box;
    border: 12px solid var(--ornament);
    outline: 4px solid var(--label-mid);
    outline-offset: -30px;
    display: flex;
    align-items: center;
    justify-content: center;
  }
  .variety-name {
    font-style: italic;
    font-weight: 400;
    font-size: 58px;
    letter-spacing: 3px;
    color: var(--ink);
  }

  /* Front label */
  .front-label {
    position: absolute;
    left: 88px;
    top: 1865px;
    width: 1037px;
    height: 1647px;
    background: linear-gradient(180deg, var(--label-dark) 0%, var(--label-mid) 40%, var(--label-light) 75%, var(--label-mid) 100%);
  }
  .band {
    position: absolute;
    left: 0;
    width: 100%;
    height: 30px;
    background: var(--band);
    opacity: 0.85;
  }
  .band--top { top: 120px; }
  .band--bottom { top: 1460px; }

  .council-mark {
    position: absolute;
    left: 435px;
    top: 0;
    width: 154px;
    height: 190px;
    background: var(--band);
    display: flex;
    flex-direction: column;
    align-items: center;
    justify-content: center;
    gap: 14px;
  }
  .council-mark__square {
    width: 36px;
    height: 36px;
    background: var(--label-dark);
  }
  .council-mark__name {
    font-weight: 700;
    font-size: 26px;
    color: var(--label-dark);
  }

  .ornament-frame {
    position: absolute;
    left: 180px;
    top: 286px;
    width: 677px;
    height: 904px;
  }
  .landscape {
    position: absolute;
    left: 274px;
    top: 397px;
    width: 488px;
    height: 715px;
  }

  .selection-text {
    position: absolute;
    left: 0;
    top: 1265px;
    width: 100%;
    text-align: center;
    font-weight: 700;
    font-size: 50px;
    line-height: 60px;
    margin: 0;
  }
  .volume, .alcohol {
    position: absolute;
    top: 1535px;
    font-weight: 700;
    font-size: 54px;
    line-height: 64px;
    margin: 0;
  }
  .volume { left: 29px; }
  .alcohol { right: 38px; }
</style>
</head>
<body>
<main class="canvas">
  <div class="neck-label">
    <span class="variety-name">FINO</span>
  </div>

  <section class="front-label">
    <div class="band band--top"></div>

    <div class="council-mark">
      <span class="council-mark__square"></span>
      <span class="council-mark__name">Velmora</span>
    </div>

    <svg class="ornament-frame" viewBox="0 0 677 904" role="img" aria-label="Decorative floral scroll wreath framing the landscape">
      <defs>
        <radialGradient id="wreathTone" cx="50%" cy="50%" r="50%">
          <stop offset="70%" stop-color="#8d6c3f" stop-opacity="0"/>
          <stop offset="85%" stop-color="#8d6c3f" stop-opacity="0.7"/>
          <stop offset="100%" stop-color="#8d6c3f" stop-opacity="0"/>
        </radialGradient>
      </defs>
      <ellipse cx="338.5" cy="452" rx="338" ry="451" fill="url(#wreathTone)"/>
    </svg>

    <svg class="landscape" viewBox="0 0 488 715" role="img" aria-label="Sepia photograph of a hillside village beneath rocky mountains">
      <defs>
        <linearGradient id="landscapeTone" x1="0" y1="0" x2="0" y2="1">
          <stop offset="0%" stop-color="#b9a27a"/>
          <stop offset="45%" stop-color="#7e6a4a"/>
          <stop offset="100%" stop-color="#4a3a24"/>
        </linearGradient>
      </defs>
      <ellipse cx="244" cy="357.5" rx="240" ry="353" fill="url(#landscapeTone)" stroke="#6a5232" stroke-width="6"/>
    </svg>

    <p class="selection-text">Vino selecionado por el Consejo Regulador<br>de la Denominacion de Origen</p>

    <div class="band band--bottom"></div>

    <p class="volume">cl 75</p>
    <p class="alcohol">15 %</p>
  </section>
</main>
</body>
</html>
```